Management Consulting needing a cool business card for client acquisition and networking

We are looking for a business card that is progressive and fresh that conveys innovation, forward thinking, and confidence. The business card is for a company based in Charlotte NC called, 'MERIDOX CONSULTING GROUP LLC'. The company primarily works with banks, insurance, and brokerages to implement innovative solutions to help them streamline their operations, to more effectively manage risks, and to improve their customer relationships.

Target Market(s)

Typically meet with Chief Financial Officers, Chief Information Officers, Chief Operations Officer, Business Unit Leader. The target market are generally 40-55 years, male, white, master level education plus.

Industry/Entity Type

Progressive

Font styles to use
Serif
Other font styles liked:
• Calibri

Requirements
Should not have
• Designs that look too much like law firms or accounting companies. Too conservative

```html
<!DOCTYPE html>
<html lang="en">
<head>
<meta charset="utf-8">
<title>Meridox Consulting Group — Business Card</title>
<link rel="stylesheet" href="https://fonts.googleapis.com/css2?family=Lato:wght@400;700&display=swap">
<style>
  :root {
    --backdrop: #3a3a3c;
    --card-blue: #0b2a78;
    --card-blue-light: #0e3288;
    --card-blue-deep: #061a57;
    --accent-red: #c8102e;
    --silver: #d4d6da;
    --white: #ffffff;
  }
  * { margin: 0; padding: 0; box-sizing: border-box; }
  html, body { width: 1200px; height: 900px; overflow: hidden; }
  body {
    background: var(--backdrop);
    font-family: "Lato", "Calibri", sans-serif;
    position: relative;
  }
  .card {
    position: absolute;
    top: 302px;
    width: 514px;
    height: 296px;
    border-radius: 18px;
    overflow: hidden;
    background: linear-gradient(135deg, var(--card-blue) 0%, var(--card-blue-light) 100%);
  }
  .card--front { left: 72px; }
  .card--back { left: 615px; }
  .card__sheen {
    position: absolute; inset: 0;
    width: 100%; height: 100%;
  }
  .brand-mark {
    position: absolute;
    border: 2px solid var(--silver);
    border-radius: 50%;
  }
  .card--front .brand-mark {
    width: 84px; height: 84px;
    left: 215px; top: 90px;
  }
  .card--front .brand-name {
    position: absolute;
    left: 0; right: 0; top: 198px;
    text-align: center;
    color: var(--silver);
    font-size: 16px;
    letter-spacing: 2.6px;
    font-weight: 400;
  }
  .card--back .brand-mark {
    width: 78px; height: 78px;
    left: 100px; top: 86px;
  }
  .brand-lockup {
    position: absolute;
    left: 30px; width: 219px; top: 172px;
    text-align: center;
    color: var(--silver);
    font-weight: 400;
  }
  .brand-lockup__name { display: block; font-size: 33px; letter-spacing: 3px; line-height: 1; }
  .brand-lockup__sub { display: block; font-size: 11.5px; letter-spacing: 1.8px; margin-top: 5px; }
  .divider {
    position: absolute;
    left: 250px; top: 80px;
    width: 1.5px; height: 138px;
    background: var(--accent-red);
  }
  .contact {
    position: absolute;
    left: 280px; top: 88px;
    color: var(--white);
  }
  .contact__name { color: var(--accent-red); font-size: 15px; letter-spacing: 0.3px; }
  .contact__title { font-size: 12.5px; font-weight: 700; margin-top: 2px; }
  .contact__list { list-style: none; margin-top: 12px; font-size: 12.5px; }
  .contact__item { display: flex; align-items: flex-start; gap: 8px; line-height: 17px; }
  .contact__item--address { margin-top: 10px; }
  .contact__icon { width: 9px; height: 9px; margin-top: 4px; flex: none; }
</style>
</head>
<body>
  <section class="card card--front">
    <svg class="card__sheen" viewBox="0 0 514 296" preserveAspectRatio="none" aria-hidden="true">
      <path d="M0 150 L0 296 L150 296 Q300 260 420 160 Q250 260 0 150 Z" fill="var(--card-blue-deep)" opacity="0.6"/>
    </svg>
    <span class="brand-mark" aria-hidden="true"></span>
    <p class="brand-name">MERIDOX CONSULTING GROUP LLC</p>
  </section>

  <section class="card card--back">
    <svg class="card__sheen" viewBox="0 0 514 296" preserveAspectRatio="none" aria-hidden="true">
      <path d="M0 150 L0 296 L150 296 Q300 260 420 160 Q250 260 0 150 Z" fill="var(--card-blue-deep)" opacity="0.6"/>
    </svg>
    <span class="brand-mark" aria-hidden="true"></span>
    <p class="brand-lockup">
      <span class="brand-lockup__name">MERIDOX</span>
      <span class="brand-lockup__sub">CONSULTING GROUP LLC</span>
    </p>
    <span class="divider" aria-hidden="true"></span>
    <div class="contact">
      <p class="contact__name">DORIAN M. VALE</p>
      <p class="contact__title">chief solutions architect</p>
      <ul class="contact__list">
        <li class="contact__item">
          <svg class="contact__icon" viewBox="0 0 10 10" aria-hidden="true"><rect x="2.5" y="0.5" width="5" height="9" rx="1" fill="none" stroke="var(--accent-red)" stroke-width="1.2"/></svg>
          <span>555 201 0182</span>
        </li>
        <li class="contact__item">
          <svg class="contact__icon" viewBox="0 0 10 10" aria-hidden="true"><rect x="0.5" y="2.5" width="9" height="6" fill="var(--accent-red)"/><path d="M0.5 2.5 L5 6 L9.5 2.5" fill="none" stroke="var(--card-blue)" stroke-width="0.8"/></svg>
          <span>dvale@meridoxconsulting.com</span>
        </li>
        <li class="contact__item contact__item--address">
          <svg class="contact__icon" viewBox="0 0 10 10" aria-hidden="true"><path d="M5 0.5 L9.5 5 L8 5 L8 9.5 L2 9.5 L2 5 L0.5 5 Z" fill="var(--accent-red)"/></svg>
          <span>1480 Alder Lane,<br>Ashford NC 28390</span>
        </li>
      </ul>
    </div>
  </section>
</body>
</html>
```